Tradeshow Banner Design (Qty2, 6'H x 2'W)

Brightwell Contractors is an Electrical, Fire Alarm, and Security Contracting company. For tradeshows, we would like 2 vertical Banners to put behind our booth. Our colors are Red, Grey & Black. I would like the Banners to be informative on what services we provide, with some appealing Graphic Design. (bwc-kmo.com)
Slogan: Safeguarding Communities Electrical, Fire & Security Solutions
Target Market(s)
Commercial Construction Clients
Industry/Entity Type
Electrical / Construction
Font styles to use
Other font styles liked:
- Aileron
Colors
EB3D1F
EC4F4E
F09395
F8D3D4
FCEDEE
Requirements
Must have
- Our Logo, Color Scheme, Brief Caption of the services we provide
Nice to have
- Appealing Imagery & a modern/simplistic design

```html
<!DOCTYPE html>
<html lang="en">
<head>
<meta charset="utf-8">
<title>Brightwell Contractors – Tradeshow Banners</title>
<link href="https://fonts.googleapis.com/css2?family=Bebas+Neue&family=Oswald:wght@300;400&display=swap" rel="stylesheet">
<style>
  :root{
    --stage:#8c8c8c;
    --red:#eb1f24;
    --ink:#111111;
    --paper:#f2f2f2;
    --text:#333333;
    --line:#555555;
    --white:#ffffff;
  }
  html,body{margin:0;padding:0;overflow:hidden}
  body{width:1200px;height:665px;background:var(--stage);position:relative}
  .banner{position:absolute;top:17px;width:210px;height:630px;display:block}
  .banner--fire{left:355px}
  .banner--security{left:635px}
  .headline,.service-title,.brand-name,.phone{font-family:"Bebas Neue",sans-serif}
  .bullet,.tagline,.address{font-family:"Oswald",sans-serif;font-weight:300}
  .headline{fill:var(--white);font-size:56px}
  .brand-name{fill:var(--white);font-size:38px}
  .tagline{fill:var(--white);font-size:11px}
  .service-title{fill:var(--red);font-size:42px}
  .bullet{fill:var(--text);font-size:20px}
  .bullet-dot{fill:var(--red)}
  .phone{fill:var(--white);font-size:60px}
  .address{fill:var(--white);font-size:19px;font-weight:400}
</style>
</head>
<body>

<svg class="banner banner--fire" viewBox="0 0 476 1428" xmlns="http://www.w3.org/2000/svg">
  <defs>
    <linearGradient id="skyA" x1="0" y1="0" x2="0" y2="1">
      <stop offset="0" stop-color="#3f67b0"/><stop offset=".5" stop-color="#4a5b78"/><stop offset="1" stop-color="#24331f"/>
    </linearGradient>
    <radialGradient id="alarmA"><stop offset="0" stop-color="#e4a27f"/><stop offset=".6" stop-color="#e23a3c"/><stop offset="1" stop-color="#f1f1f1"/></radialGradient>
    <radialGradient id="techA"><stop offset="0" stop-color="#6b5a45"/><stop offset="1" stop-color="#2b2f36"/></radialGradient>
  </defs>
  <rect class="panel" width="476" height="1428" fill="var(--paper)"/>
  <path d="M0 0H476V360Q238 560 0 360Z" fill="var(--red)"/>
  <path d="M0 0H476V320Q238 540 0 320Z" fill="url(#skyA)" role="img" aria-label="Photo of a modern apartment complex at dusk"/>
  <path d="M0 385Q238 590 476 385" fill="none" stroke="var(--line)" stroke-width="1.5"/>
  <circle cx="160" cy="92" r="52" fill="var(--red)"/>
  <text class="brand-name" x="222" y="84">BRIGHTWELL</text>
  <text class="brand-name" x="222" y="120">CONTRACTORS</text>
  <text class="tagline" x="223" y="138">ELECTRICAL | FIRE | SECURITY</text>
  <text class="headline" x="238" y="305" text-anchor="middle">WE HELP OUR CLIENTS</text>
  <text class="headline" x="238" y="365" text-anchor="middle">GET PEACE OF MIND</text>

  <rect x="138" y="420" width="200" height="110" fill="var(--red)"/>
  <path d="M125 452Q240 475 352 452" fill="none" stroke="var(--ink)" stroke-width="6"/>

  <circle cx="239" cy="630" r="165" fill="none" stroke="var(--line)" stroke-width="1.5"/>
  <circle cx="239" cy="630" r="140" fill="var(--red)"/>
  <circle cx="239" cy="630" r="129" fill="url(#alarmA)" role="img" aria-label="Photo of a hand pulling a red fire alarm station"/>
  <path d="M165 775Q239 805 313 775" fill="none" stroke="var(--ink)" stroke-width="6"/>
  <text class="service-title" x="238" y="838" text-anchor="middle">FIRE PROTECTION</text>
  <circle class="bullet-dot" cx="156" cy="856" r="7"/><text class="bullet" x="174" y="863">Fire Alarm Systems</text>
  <circle class="bullet-dot" cx="85" cy="883" r="7"/><text class="bullet" x="103" y="890">Fire Inspections &amp; Confidence Testing</text>

  <path d="M440 705A70 70 0 0 0 440 835" fill="none" stroke="var(--red)" stroke-width="6"/>
  <path d="M424 705A75 75 0 0 0 424 835" fill="none" stroke="var(--ink)" stroke-width="3"/>
  <path d="M0 1140A70 70 0 0 1 0 1270" fill="none" stroke="var(--red)" stroke-width="6"/>
  <path d="M40 1150A75 75 0 0 1 40 1265" fill="none" stroke="var(--ink)" stroke-width="3"/>

  <circle cx="239" cy="1050" r="165" fill="none" stroke="var(--line)" stroke-width="1.5"/>
  <circle cx="239" cy="1050" r="140" fill="var(--red)"/>
  <circle cx="239" cy="1050" r="129" fill="url(#techA)" role="img" aria-label="Photo of an electrician wiring a panel"/>
  <path d="M165 1195Q239 1225 313 1195" fill="none" stroke="var(--ink)" stroke-width="6"/>
  <text class="service-title" x="238" y="1253" text-anchor="middle">FIRE PROTECTION</text>
  <circle class="bullet-dot" cx="115" cy="1270" r="7"/><text class="bullet" x="132" y="1277">Electrical Installation &amp; Repair</text>
  <circle class="bullet-dot" cx="163" cy="1297" r="7"/><text class="bullet" x="180" y="1304">Structured Wiring</text>

  <rect y="1318" width="476" height="14" fill="var(--ink)"/>
  <rect y="1332" width="476" height="96" fill="var(--red)"/>
  <text class="phone" x="238" y="1388" text-anchor="middle">555-014-2280</text>
  <text class="address" x="238" y="1414" text-anchor="middle">780 Harbor Ridge Rd STE 210 Kenmore, WA 98028</text>
</svg>

<svg class="banner banner--security" viewBox="0 0 476 1428" xmlns="http://www.w3.org/2000/svg">
  <defs>
    <linearGradient id="skyB" x1="0" y1="0" x2="0" y2="1">
      <stop offset="0" stop-color="#3f67b0"/><stop offset=".5" stop-color="#4a5b78"/><stop offset="1" stop-color="#24331f"/>
    </linearGradient>
    <radialGradient id="accessB"><stop offset="0" stop-color="#f7f7f7"/><stop offset=".7" stop-color="#e6e6e6"/><stop offset="1" stop-color="#c9c9c9"/></radialGradient>
    <linearGradient id="warehouseB" x1="0" y1="0" x2="1" y2="1"><stop offset="0" stop-color="#5a6fa6"/><stop offset=".5" stop-color="#c9893f"/><stop offset="1" stop-color="#d9d9d9"/></linearGradient>
  </defs>
  <rect class="panel" width="476" height="1428" fill="var(--paper)"/>
  <path d="M0 0H476V360Q238 560 0 360Z" fill="var(--red)"/>
  <path d="M0 0H476V320Q238 540 0 320Z" fill="url(#skyB)" role="img" aria-label="Photo of a modern apartment complex at dusk"/>
  <path d="M0 385Q238 590 476 385" fill="none" stroke="var(--line)" stroke-width="1.5"/>
  <circle cx="160" cy="92" r="52" fill="var(--red)"/>
  <text class="brand-name" x="222" y="84">BRIGHTWELL</text>
  <text class="brand-name" x="222" y="120">CONTRACTORS</text>
  <text class="tagline" x="223" y="138">ELECTRICAL | FIRE | SECURITY</text>
  <text class="headline" x="238" y="305" text-anchor="middle" font-size="52">LET US HELP YOU PROTECT</text>
  <text class="headline" x="238" y="360" text-anchor="middle" font-size="52">YOUR BUSINESS TODAY.</text>

  <rect x="138" y="420" width="200" height="110" fill="var(--red)"/>
  <path d="M125 452Q240 475 352 452" fill="none" stroke="var(--ink)" stroke-width="6"/>

  <circle cx="239" cy="630" r="165" fill="none" stroke="var(--line)" stroke-width="1.5"/>
  <circle cx="239" cy="630" r="140" fill="var(--red)"/>
  <circle cx="239" cy="630" r="129" fill="url(#accessB)" role="img" aria-label="Photo of a woman using a wall-mounted access reader"/>
  <path d="M165 775Q239 805 313 775" fill="none" stroke="var(--ink)" stroke-width="6"/>
  <text class="service-title" x="238" y="846" text-anchor="middle">SECURITY</text>
  <circle class="bullet-dot" cx="2256" cy="864" r="7" transform="translate(-2000 0)"/><text class="bullet" x="273" y="871">Security Monitoring</text>

  <path d="M0 700A70 70 0 0 1 0 830" fill="none" stroke="var(--red)" stroke-width="6"/>
  <path d="M40 710A75 75 0 0 1 40 825" fill="none" stroke="var(--ink)" stroke-width="3"/>
  <path d="M476 1140A70 70 0 0 0 476 1270" fill="none" stroke="var(--red)" stroke-width="6"/>
  <path d="M436 1150A75 75 0 0 0 436 1265" fill="none" stroke="var(--ink)" stroke-width="3"/>

  <circle cx="239" cy="1050" r="165" fill="none" stroke="var(--line)" stroke-width="1.5"/>
  <circle cx="239" cy="1050" r="140" fill="var(--red)"/>
  <circle cx="239" cy="1050" r="129" fill="url(#warehouseB)" role="img" aria-label="Photo of a dome security camera in a warehouse"/>
  <path d="M165 1195Q239 1225 313 1195" fill="none" stroke="var(--ink)" stroke-width="6"/>
  <text class="service-title" x="238" y="1260" text-anchor="middle">SURVEILLANCE</text>

  <rect y="1318" width="476" height="14" fill="var(--ink)"/>
  <rect y="1332" width="476" height="96" fill="var(--red)"/>
  <text class="phone" x="238" y="1388" text-anchor="middle">555-014-2280</text>
  <text class="address" x="238" y="1414" text-anchor="middle">780 Harbor Ridge Rd STE 210 Kenmore, WA 98028</text>
</svg>

</body>
</html>
```